Business card design needed

We do excavation, cartage and contracting
I would quote like to have a picture of my digger as the whole back ground and the words on top. If that looks any good
Otherwise please feel free to come up with any other cool options

Cheers Marc

KLR Contracting
Excavation, Cartage, Contracting
Marcus Prewitt
www.klr-example.co.nz
021 584 067
marc@klr-example.co.nz

```html
<!DOCTYPE html>
<html lang="en">
<head>
<meta charset="utf-8">
<title>KLR Contracting – Business Card</title>
<link rel="stylesheet" href="https://fonts.googleapis.com/css2?family=Tinos&display=swap">
<style>
  :root {
    --paper: #ffffff;
    --ink: #0d0d0d;
    --brand-green: #2f5a1c;
    --reverse-text: #ffffff;
  }
  * { margin: 0; padding: 0; box-sizing: border-box; }
  html, body {
    width: 1200px;
    height: 741px;
    overflow: hidden;
    background: var(--paper);
  }
  .card {
    position: relative;
    width: 1200px;
    height: 741px;
    background: var(--paper);
    font-family: "Tinos", "Times New Roman", serif;
    overflow: hidden;
  }
  .ground-art {
    position: absolute;
    inset: 0;
    width: 1200px;
    height: 741px;
  }
  .ground-art path { fill: var(--ink); }
  .brand-name {
    position: absolute;
    left: 44px;
    top: 95px;
    width: 360px;
    text-align: center;
    color: var(--brand-green);
    font-size: 150px;
    line-height: 1;
  }
  .owner {
    position: absolute;
    left: 600px;
    top: 118px;
    width: 650px;
    text-align: center;
    color: var(--ink);
  }
  .owner-name {
    font-size: 104px;
    line-height: 1;
    transform: scaleX(0.72);
    transform-origin: center;
    white-space: nowrap;
  }
  .owner-role {
    margin-top: 14px;
    font-size: 40px;
    line-height: 1;
    transform: scaleX(0.8);
    transform-origin: center;
    letter-spacing: 0.5px;
  }
  .contact {
    position: absolute;
    left: 0;
    width: 1200px;
    text-align: center;
    color: var(--reverse-text);
    font-size: 48px;
    line-height: 1;
    white-space: nowrap;
  }
  .contact-services {
    top: 594px;
    transform: scaleX(0.86);
    transform-origin: center;
  }
  .contact-direct { top: 665px; }
</style>
</head>
<body>
  <div class="card">
    <svg class="ground-art" viewBox="0 0 1200 741" role="img"
         aria-label="Black silhouette of an excavator arm digging into a mound of earth, spanning the lower card">
      <path d="M0 470 C 60 420, 110 382, 200 376 C 320 368, 430 382, 520 460 C 600 525, 800 532, 1200 535 L 1200 741 L 0 741 Z"/>
    </svg>

    <div class="brand-name">KLR</div>

    <div class="owner">
      <div class="owner-name">Marcus Prewitt</div>
      <div class="owner-role">CONTRACTOR</div>
    </div>

    <div class="contact contact-services">KLR Contracting Excavation • Cartagewww.klr-example.co.nz</div>
    <div class="contact contact-direct">021 584 067 &nbsp;• marc@klr-example.co.nz</div>
  </div>
</body>
</html>
```